Business Card of PebbleFinch
PebbleFinch
Bright & Fun-filled
Daniel Osei, CFA
President
412 Whitmore Suite 208
Irvine, CA 92655
daniel@pebblefinch.example
pebblefinch.example

```html
<!DOCTYPE html>
<html lang="en">
<head>
<meta charset="utf-8">
<title>PebbleFinch Stationery Set</title>
<link href="https://fonts.googleapis.com/css2?family=Nunito:wght@700;800&display=swap" rel="stylesheet">
<style>
  :root {
    --brand-red: #e32b2b;
    --brand-yellow: #f6b419;
    --paper: #ffffff;
    --ink: #555555;
    --rule: #d9d9d9;
    --shadow: rgba(0,0,0,0.12);
  }
  html, body { margin: 0; padding: 0; overflow: hidden; background: var(--paper); }
  .canvas { display: block; width: 1200px; height: 248px; }
  .brand-name { font-family: "Nunito", sans-serif; font-weight: 800; fill: var(--brand-red); }
  .body-text { font-family: "Nunito", sans-serif; font-weight: 700; fill: var(--ink); }
  .fax-title { font-family: "Nunito", sans-serif; font-weight: 800; fill: var(--ink); }
  .sheet { fill: var(--paper); stroke: var(--rule); stroke-width: 1; filter: drop-shadow(1px 1px 1.5px var(--shadow)); }
  .band-red { fill: var(--brand-red); }
  .band-yellow { fill: var(--brand-yellow); }
  .mark-dot { fill: var(--brand-yellow); }
  .rule-line { stroke: var(--rule); stroke-width: 1; }
  .frame { fill: none; stroke: var(--brand-red); stroke-width: 6; }
</style>
</head>
<body>
<svg class="canvas" viewBox="0 0 1200 248" xmlns="http://www.w3.org/2000/svg">
  <defs>
    <g id="brand-lockup">
      <circle class="mark-dot" cx="0" cy="-3" r="5"/>
      <text class="brand-name" x="8" y="0" font-size="9">PebbleFinch</text>
    </g>
  </defs>

  <rect class="frame" x="3" y="3" width="1194" height="242"/>

  <!-- Business card, front -->
  <g class="business-card-front">
    <rect class="sheet" x="29" y="53" width="91" height="58"/>
    <path class="band-yellow" d="M92 53 H120 V111 H78 Q104 86 92 53 Z"/>
    <path class="band-red" d="M104 53 H120 V111 H96 Q116 84 104 53 Z"/>
    <use href="#brand-lockup" x="40" y="86"/>
  </g>

  <!-- Business card, back -->
  <g class="business-card-back">
    <rect class="sheet" x="29" y="125" width="91" height="58"/>
    <use href="#brand-lockup" x="36" y="138" transform="translate(0,0)"/>
    <text class="body-text" x="36" y="152" font-size="4.5">Daniel Osei, CFA · President</text>
    <text class="body-text" x="36" y="159" font-size="3.6">412 Whitmore Suite 208, Irvine, CA 92655</text>
    <text class="body-text" x="36" y="165" font-size="3.6">daniel@pebblefinch.example</text>
    <path class="band-yellow" d="M29 183 V174 Q75 164 120 172 V183 Z"/>
    <path class="band-red" d="M29 183 V178 Q75 170 120 178 V183 Z"/>
  </g>

  <!-- Letterhead -->
  <g class="letterhead">
    <rect class="sheet" x="149" y="43" width="91" height="178"/>
    <path class="band-yellow" d="M196 43 H240 V70 Q220 52 196 43 Z"/>
    <path class="band-red" d="M212 43 H240 V62 Q228 49 212 43 Z"/>
    <use href="#brand-lockup" x="156" y="58"/>
    <line class="rule-line" x1="158" y1="90" x2="230" y2="90"/>
    <line class="rule-line" x1="158" y1="98" x2="230" y2="98"/>
    <line class="rule-line" x1="158" y1="106" x2="220" y2="106"/>
    <path class="band-yellow" d="M149 221 V208 Q195 196 240 206 V221 Z"/>
    <path class="band-red" d="M149 221 V214 Q195 204 240 213 V221 Z"/>
  </g>

  <!-- Compliment slip -->
  <g class="compliment-slip">
    <rect class="sheet" x="257" y="53" width="67" height="43"/>
    <path class="band-yellow" d="M300 53 H324 V96 H292 Q314 76 300 53 Z"/>
    <path class="band-red" d="M310 53 H324 V96 H306 Q322 74 310 53 Z"/>
  </g>

  <!-- Card stack -->
  <g class="card-stack">
    <rect class="sheet" x="262" y="115" width="72" height="43"/>
    <use href="#brand-lockup" x="272" y="139"/>
    <rect class="sheet" x="262" y="175" width="72" height="43"/>
    <path class="band-yellow" d="M262 218 V208 Q298 200 334 206 V218 Z"/>
    <path class="band-red" d="M262 218 V213 Q298 206 334 212 V218 Z"/>
  </g>

  <!-- Envelopes -->
  <g class="envelopes">
    <rect class="sheet" x="360" y="100" width="120" height="30"/>
    <path class="band-red" d="M360 100 L420 118 L480 100 Z"/>
    <path class="band-yellow" d="M360 130 V122 Q420 112 480 122 V130 Z"/>
    <rect class="sheet" x="360" y="142" width="120" height="55"/>
    <use href="#brand-lockup" x="370" y="160"/>
    <path class="band-yellow" d="M360 197 V188 Q420 178 480 188 V197 Z"/>
    <rect class="sheet" x="490" y="100" width="100" height="90"/>
    <path class="band-yellow" d="M490 100 L540 140 L590 100 Z"/>
    <path class="band-red" d="M490 100 L540 128 L590 100 Z"/>
  </g>

  <!-- Presentation folder -->
  <g class="presentation-folder">
    <rect class="sheet" x="624" y="43" width="162" height="178"/>
    <path class="band-yellow" d="M624 43 H786 V66 Q705 42 624 72 Z"/>
    <path class="band-red" d="M624 43 H786 V54 Q705 36 624 60 Z"/>
    <use href="#brand-lockup" x="680" y="128"/>
    <rect class="sheet" x="786" y="43" width="162" height="178"/>
    <path class="band-yellow" d="M786 140 Q867 118 948 140 V221 H786 Z"/>
    <path class="band-red" d="M786 221 V210 Q867 198 948 210 V221 Z"/>
    <rect class="sheet" x="830" y="128" width="72" height="43"/>
    <use href="#brand-lockup" x="838" y="152"/>
  </g>

  <!-- Disc and sleeve -->
  <g class="disc-sleeve">
    <rect class="sheet" x="952" y="60" width="110" height="130"/>
    <circle class="sheet" cx="1010" cy="115" r="40"/>
    <path class="band-yellow" d="M975 128 A40 40 0 0 0 1045 128 Z"/>
    <circle fill="#ffffff" stroke="#d9d9d9" cx="1010" cy="115" r="8"/>
  </g>

  <!-- Fax sheet -->
  <g class="fax-sheet">
    <rect class="sheet" x="1068" y="48" width="108" height="174"/>
    <text class="fax-title" x="1078" y="78" font-size="14">Fax</text>
    <text class="body-text" x="1078" y="96" font-size="4.5">To</text>
    <line class="rule-line" x1="1095" y1="96" x2="1166" y2="96"/>
    <text class="body-text" x="1078" y="106" font-size="4.5">From</text>
    <line class="rule-line" x1="1095" y1="106" x2="1166" y2="106"/>
    <text class="body-text" x="1078" y="116" font-size="4.5">Date</text>
    <line class="rule-line" x1="1095" y1="116" x2="1166" y2="116"/>
    <text class="body-text" x="1078" y="126" font-size="4.5">Pages</text>
    <line class="rule-line" x1="1095" y1="126" x2="1166" y2="126"/>
    <line class="rule-line" x1="1078" y1="140" x2="1166" y2="140"/>
    <use href="#brand-lockup" x="1078" y="212"/>
  </g>
</svg>
</body>
</html>
```